A farm is looking for the unified design for the bags' and bottles' labels in their organic produ...

We are a farm that deals with the production and sale of the organic seeds and oils. From the seed programme, we offer the organic flax, sunflower, hemp and pumpkin seeds. In our program, the organic unrefined cold-pressed hemp, linseed and sunflower oil and cold-pressed pumpkin oil can be found.
Design wise, we want to unify our sales programme with a unique organic look of bottle labels containing organic oils and labels for paper bags containing seeds.
We intend to keep the appearance of the exiting logotype (refer to the logotype provided in the enclosed PDF file). Regarding the colours, our products should be separated by a colour scheme (hemp, flax, pumpkin seeds, sunflower, etc.). The label material should be the same for the bags and the bottles. If possible, we would like to utilize the ecological paper, together with the option of applying the labels using the organic glue (starch, etc.). Also, the possibility of the eventual later printing directly onto the packaging (paper bags and bottles) must be considered and envisioned.
Additionally, there should be space on the label for the written title of the product (for example, »BIO pumpkin seeds«) and some space for short indications, markings and data in the corners of the label. You can also include an image that will indicate the contents of the bag/bottle.
We will appreciate all your contributions.

IN DOMESTIC LANGUAGE:
Smo kmetija, ki se ukvarja s pridelavo in prodajo ekoloških semen in olj. Iz programa semen nudimo BIO lanena, sončnična, konopljina in bučna semena. V našem programu so BIO nerafinirano hladno stiskano konopljino, laneno ter sončnično olje in hladno stiskano bučno olje.
Želimo oblikovno poenotiti naš prodajni program z enotnim EKO videzom etiket za steklenice z BIO olji in etiket za papirnate vrečke z semeni.
Ohraniti nameravamo videz obstoječega logotipa (glej logotip v priloženi PDF datoteki). Barvno je treba ločiti proizvode po barvni shemi (konoplja, lan, bučno seme, sončnica …). Material etiket naj bo enak za vrečke in steklenice. Po možnosti naj gre za ekološki papir, pa tudi možnost nanosa etiket z ekološkim lepilom (škrob …). Predvideti je treba tudi možen kasnejši tisk neposredno na embalažo (papirnate vrečke ter steklenice).
Prav tako naj bo na etiketi prostor za napis naslova izdelka (na primer »BIO bučno seme«) in po robovih nekaj prostora za krajše navedbe, označbe ter podatke, vključena pa je lahko tudi slika, ki nakazuje na vsebino vrečke/steklenice.
Najlepša hvala že vnaprej za vaše prispevke.

```html
<!DOCTYPE html>
<html lang="en">
<head>
<meta charset="utf-8">
<title>Organic Seed Label System</title>
<link rel="stylesheet" href="https://fonts.googleapis.com/css2?family=Questrial&display=swap">
<style>
  :root {
    --canvas: #ffffff;
    --panel-line: #a9a9a9;
    --note-ink: #1a1a1a;
    --flax-band: #6a1915;
    --flax-seed-a: #b67a52;
    --flax-seed-b: #8a4e2e;
    --flax-ink: #4a2b1c;
    --sun-band: #0c6a35;
    --sun-seed-a: #5a5a5a;
    --sun-seed-b: #2a2a2a;
    --hemp-band: #0c6a35;
    --hemp-seed-a: #bba578;
    --hemp-seed-b: #8c784f;
    --pumpkin-band: #d9590b;
    --pumpkin-seed-a: #e6dccb;
    --pumpkin-seed-b: #c5b497;
    --label-ink: #2b3322;
  }
  * { margin: 0; padding: 0; box-sizing: border-box; }
  html, body { width: 1200px; height: 999px; overflow: hidden; background: var(--canvas); }
  .canvas { position: relative; width: 1200px; height: 999px; font-family: "Questrial", sans-serif; }
  .showcase-frame, .callouts { position: absolute; left: 0; top: 0; }
  .label { position: absolute; display: block; }
  .label--flax { --band: var(--flax-band); --ink: var(--flax-ink); }
  .label--sunflower { --band: var(--sun-band); --ink: var(--label-ink); }
  .label--hemp { --band: var(--hemp-band); --ink: var(--label-ink); }
  .label--pumpkin { --band: var(--pumpkin-band); --ink: var(--label-ink); }
  .label-title { font-family: "Questrial", sans-serif; font-size: 13px; fill: var(--ink); }
  .callout {
    position: absolute; color: var(--note-ink); font-size: 22px; line-height: 26px; text-align: center;
    font-family: "Questrial", sans-serif;
  }
</style>
</head>
<body>
<main class="canvas">

  <svg width="0" height="0" style="position:absolute" aria-hidden="true">
    <defs>
      <symbol id="label-base" viewBox="0 0 345 424">
        <path d="M0,424 V40 Q0,0 40,0 H305 Q345,0 345,40 V424 Z" style="fill: var(--bg)"/>
        <rect x="10" y="12" width="325" height="360" rx="30" fill="none" stroke="#fff" stroke-width="1.5"/>
        <rect x="137" y="0" width="71" height="44" style="fill: var(--band)"/>
        <line x1="95" y1="64" x2="250" y2="64" stroke-width="1" style="stroke: var(--band)"/>
        <line x1="95" y1="88" x2="250" y2="88" stroke-width="1" style="stroke: var(--band)"/>
        <rect x="0" y="196" width="345" height="30" style="fill: var(--band)"/>
        <rect x="0" y="384" width="345" height="40" style="fill: var(--band)"/>
      </symbol>
      <radialGradient id="bg-flax" cx="0.5" cy="0.4" r="0.75"><stop offset="0" stop-color="#f6e6c8"/><stop offset="1" stop-color="#d8b88a"/></radialGradient>
      <radialGradient id="bg-sunflower" cx="0.5" cy="0.45" r="0.75"><stop offset="0" stop-color="#fcea7e"/><stop offset="1" stop-color="#f2c01c"/></radialGradient>
      <radialGradient id="bg-hemp" cx="0.5" cy="0.45" r="0.75"><stop offset="0" stop-color="#c0e08a"/><stop offset="1" stop-color="#6cab38"/></radialGradient>
      <radialGradient id="bg-pumpkin" cx="0.5" cy="0.45" r="0.75"><stop offset="0" stop-color="#ffd66a"/><stop offset="1" stop-color="#f8a812"/></radialGradient>
      <radialGradient id="seed-flax"><stop offset="0" stop-color="var(--flax-seed-a)"/><stop offset="1" stop-color="var(--flax-seed-b)"/></radialGradient>
      <radialGradient id="seed-sunflower"><stop offset="0" stop-color="var(--sun-seed-a)"/><stop offset="1" stop-color="var(--sun-seed-b)"/></radialGradient>
      <radialGradient id="seed-hemp"><stop offset="0" stop-color="var(--hemp-seed-a)"/><stop offset="1" stop-color="var(--hemp-seed-b)"/></radialGradient>
      <radialGradient id="seed-pumpkin"><stop offset="0" stop-color="var(--pumpkin-seed-a)"/><stop offset="1" stop-color="var(--pumpkin-seed-b)"/></radialGradient>
    </defs>
  </svg>

  <svg class="showcase-frame" width="760" height="500" aria-hidden="true">
    <path d="M748,0 V465 Q748,495 718,495 H0" fill="none" stroke="var(--panel-line)" stroke-width="3"/>
  </svg>

  <svg class="label label--flax" style="left:76px;top:232px;--bg:url(#bg-flax)" width="136" height="178" viewBox="0 0 345 424" preserveAspectRatio="none">
    <use href="#label-base"/>
    <text class="label-title" x="172.5" y="81" text-anchor="middle">ORGANIC FLAX SEED</text>
    <circle cx="172.5" cy="232" r="112" fill="url(#seed-flax)" role="img" aria-label="Photo of flax seeds"/>
    <circle cx="172.5" cy="232" r="66" fill="#fff"/>
  </svg>
  <svg class="label label--sunflower" style="left:300px;top:175px;--bg:url(#bg-sunflower)" width="176" height="223" viewBox="0 0 345 424" preserveAspectRatio="none">
    <use href="#label-base"/>
    <text class="label-title" x="172.5" y="81" text-anchor="middle">ORGANIC SUNFLOWER SEED</text>
    <circle cx="172.5" cy="232" r="112" fill="url(#seed-sunflower)" role="img" aria-label="Photo of sunflower seeds"/>
    <circle cx="172.5" cy="232" r="66" fill="#fff"/>
  </svg>

  <svg class="callouts" width="760" height="500" aria-hidden="true">
    <g fill="none" stroke="#111" stroke-width="2">
      <path d="M392,190 C430,140 480,128 538,128"/>
      <path d="M402,285 C450,262 490,256 538,256"/>
      <path d="M402,390 C450,400 490,398 538,395"/>
    </g>
    <g fill="#111">
      <polygon points="544,128 534,123 534,133"/>
      <polygon points="544,256 534,251 534,261"/>
      <polygon points="544,395 534,390 534,400"/>
    </g>
  </svg>
  <p class="callout" style="left:540px;top:114px;width:188px;">Your Brand Logo<br>Here</p>
  <p class="callout" style="left:540px;top:230px;width:158px;">Title of<br>the Product</p>
  <p class="callout" style="left:536px;top:363px;width:196px;">Short Information<br>or Data</p>

  <svg class="label label--flax" style="left:810px;top:52px;--bg:url(#bg-flax)" width="345" height="424" viewBox="0 0 345 424">
    <use href="#label-base"/>
    <text class="label-title" x="172.5" y="81" text-anchor="middle">ORGANIC FLAX SEED</text>
    <circle cx="172.5" cy="232" r="112" fill="url(#seed-flax)" role="img" aria-label="Photo of flax seeds"/>
    <circle cx="172.5" cy="232" r="66" fill="#fff"/>
  </svg>
  <svg class="label label--sunflower" style="left:46px;top:523px;--bg:url(#bg-sunflower)" width="345" height="424" viewBox="0 0 345 424">
    <use href="#label-base"/>
    <text class="label-title" x="172.5" y="81" text-anchor="middle">ORGANIC SUNFLOWER SEED</text>
    <circle cx="172.5" cy="232" r="112" fill="url(#seed-sunflower)" role="img" aria-label="Photo of sunflower seeds"/>
    <circle cx="172.5" cy="232" r="66" fill="#fff"/>
  </svg>
  <svg class="label label--hemp" style="left:429px;top:523px;--bg:url(#bg-hemp)" width="345" height="424" viewBox="0 0 345 424">
    <use href="#label-base"/>
    <text class="label-title" x="172.5" y="81" text-anchor="middle">ORGANIC HEMP SEED</text>
    <circle cx="172.5" cy="232" r="112" fill="url(#seed-hemp)" role="img" aria-label="Photo of hemp seeds"/>
    <circle cx="172.5" cy="232" r="66" fill="#fff"/>
  </svg>
  <svg class="label label--pumpkin" style="left:810px;top:523px;--bg:url(#bg-pumpkin)" width="345" height="424" viewBox="0 0 345 424">
    <use href="#label-base"/>
    <text class="label-title" x="172.5" y="81" text-anchor="middle">ORGANIC PUMPKIN SEED</text>
    <circle cx="172.5" cy="232" r="112" fill="url(#seed-pumpkin)" role="img" aria-label="Photo of pumpkin seeds"/>
    <circle cx="172.5" cy="232" r="66" fill="#fff"/>
  </svg>

</main>
</body>
</html>
```